BrightHarbor is a fund management company that takes just four market positions a year. each position is linked to a big geopolitical and economic event happening in the world. So for example we may be buying gold mining stocks-these are the companies who dig the gold out of the ground, as all the gold is currently being bought by Asia, or buying the japanese stock market as this is one of the big stories of today.

I am looking for a logo that represents 'BrightHarbor'-the Bright Harbor.

I would like it to be small and sit to the left of the name of the company on the left hand side(I think!)on the top line of the business card please.

Industry/Entity Type

Mining

Contact Information for Business Card

BrightHarbor Investment management Ltd
41 Fennick Lane
London E9 7QT

Tomas P Hulme

Mob: 0(44)7839254086
Off: 0(44) 203 xxxx
email: th@brightharbor-fm.example

```html
<!DOCTYPE html>
<html lang="en">
<head>
<meta charset="utf-8">
<title>BrightHarbor – Business Card &amp; Logo</title>
<link rel="stylesheet" href="https://fonts.googleapis.com/css2?family=Baloo+2:wght@400;600;700&family=Arimo:wght@700&display=swap">
<style>
  :root{
    --stage:#bcbdc0;
    --paper:#ffffff;
    --navy:#2b2a6e;
    --sky:#cfe6ef;
    --sky-deep:#a9d3e4;
    --globe:#2aa3d6;
    --green:#7fb04a;
    --green-soft:#9bc46d;
    --purple:#3a2f72;
  }
  *{margin:0;padding:0;box-sizing:border-box}
  html,body{width:1200px;height:1200px;overflow:hidden}
  body{position:relative;background:var(--paper);font-family:"Baloo 2",sans-serif;color:var(--navy)}

  .stage{position:absolute;left:0;top:0;width:1200px;height:858px;background:var(--stage)}

  .card{position:absolute;left:92px;top:87px;width:690px;height:391px;background:var(--paper);
    box-shadow:3px 4px 6px rgba(0,0,0,.35);overflow:hidden}
  .card__map{position:absolute;right:0;top:0;width:345px;height:391px;
    background:radial-gradient(ellipse at 60% 45%,var(--sky) 0%,#e4f1f6 55%,rgba(255,255,255,0) 80%)}
  .card__brand{position:absolute;left:38px;top:24px;display:flex;align-items:center;gap:10px}
  .mark-dot{width:62px;height:62px;border-radius:50%;background:var(--globe);flex:none}
  .brand-name{font-weight:700;font-size:40px;line-height:1;color:var(--navy)}
  .brand-sub{font-weight:400;font-size:16px;line-height:1.2;color:var(--navy)}
  .card__name{position:absolute;left:41px;top:170px;font-weight:700;font-size:26px}
  .contact{position:absolute;left:41px;top:220px;display:grid;grid-template-columns:58px 1fr;
    column-gap:24px;font-size:21px;line-height:30px}
  .contact dt{font-weight:700;text-align:right}
  .contact dd{font-weight:400}
  .contact .gap{margin-bottom:0}

  .logos{position:absolute;left:0;top:858px;width:1200px;height:342px}
  .logo{position:absolute;display:flex;align-items:center}
  .logo--primary{left:438px;top:38px;gap:12px}
  .logo--primary .mark-dot{width:100px;height:100px}
  .logo--primary .brand-name{font-size:48px}
  .logo--primary .brand-sub{font-size:20px}
  .logo--green{left:118px;top:226px;gap:20px}
  .logo--green .mark-dot{width:84px;height:84px;background:var(--green-soft)}
  .block-name{font-family:"Arimo",sans-serif;font-weight:700;font-size:44px;line-height:1}
  .block-sub{font-family:"Arimo",sans-serif;font-weight:700;font-size:18px;line-height:1.3}
  .logo--green .block-name,.logo--green .block-sub{color:var(--green)}
  .logo--navy{left:626px;top:203px;gap:14px}
  .logo--navy .mark-dot{width:110px;height:110px;background:var(--purple)}
  .logo--navy .block-name{color:var(--navy);font-size:50px}
  .logo--navy .block-sub{color:var(--navy)}
</style>
</head>
<body>
  <section class="stage">
    <article class="card">
      <div class="card__map" role="img" aria-label="Faint light-blue world map with globe grid lines showing Europe and Africa"></div>
      <div class="card__brand">
        <span class="mark-dot"></span>
        <div>
          <div class="brand-name">BrightHarbor</div>
          <div class="brand-sub">Investment Management Ltd</div>
        </div>
      </div>
      <h1 class="card__name">Tomas P Hulme</h1>
      <dl class="contact">
        <dt>a:</dt><dd>41 Fennick Lane, London<br>E9 7QT, United Kingdom</dd>
        <dt>mob:</dt><dd>0(44) 783 925 4086</dd>
        <dt>off:</dt><dd>0(44) 203 0000</dd>
        <dt>e:</dt><dd>th@brightharbor-fm.example</dd>
      </dl>
    </article>
  </section>

  <section class="logos">
    <div class="logo logo--primary">
      <span class="mark-dot"></span>
      <div>
        <div class="brand-name">BrightHarbor</div>
        <div class="brand-sub">Investment Management Ltd</div>
      </div>
    </div>
    <div class="logo logo--green">
      <span class="mark-dot"></span>
      <div>
        <div class="block-name">BRIGHT HARBOR</div>
        <div class="block-sub">INVESTMENT MANAGEMENT LTD</div>
      </div>
    </div>
    <div class="logo logo--navy">
      <span class="mark-dot"></span>
      <div>
        <div class="block-name">BRIGHTHARBOR</div>
        <div class="block-sub">INVESTMENT MANAGEMENT LTD</div>
      </div>
    </div>
  </section>
</body>
</html>
```